Redesign wellness clinic website

The project is redesign a wellness clinic http://www.thornleighvitality.example. The new website is to be responsive,clean,bright and a strong call to action which is to book an appointment. The logo will remain the same but the colour scheme on the website should be reflect purple white and green. I want it to be bright and cheerful and the feeling of clarity. The website shouldn't be overloaded with content but more visuals.

Target Market(s)

Anyone that has corporate wellness benefits within the downtown Toronto core. Majority of audience are professional working in Media, Telecommunications and Investments.

Industry/Entity Type

Health And Wellness

Number of Pages Required

5+ page

Font styles to use
Sans Serif

Colors
ffffff
886aae
acd036

Requirements
Must have
• -Strong call to action which is book an appointment like this page https://www.kestrelmotion.example/
• -Services provided icons on the page like https://www.brightpathvitalityhouse.example/
• - Pictures of a good visualizing a fit and healthy life
• - Strong ratings from Quorva, Zintrel, PostMaz, similar to this website http://www.summitbalancehealth.example/our-team-professionals/
• - Bright and clear
Should not have
• -No black and white images (redo our pictures)
• -Dark themes

```html
<!DOCTYPE html>
<html lang="en">
<head>
<meta charset="utf-8">
<title>Thornleigh Vitality Centre</title>
<link href="https://fonts.googleapis.com/css2?family=Open+Sans:wght@400;600&family=Titillium+Web:wght@600;700;900&display=swap" rel="stylesheet">
<style>
:root{
  --purple:#886aae;
  --purple-deep:#6e2c7f;
  --purple-soft:#a58bc4;
  --green:#acd036;
  --green-soft:#c0dc6a;
  --green-pale:#f2f7e1;
  --white:#ffffff;
  --text:#555555;
  --nav:#555555;
}
*{box-sizing:border-box;margin:0;padding:0}
html,body{width:1079px;height:1200px;overflow:hidden;background:var(--white)}
body{font-family:"Open Sans",sans-serif;color:var(--text);position:relative}
.topbar{position:absolute;left:0;top:0;width:1079px;height:102px;background:var(--green-pale)}
.hours{position:absolute;left:84px;top:7px;font-size:10.5px;color:#555;display:flex;align-items:center;gap:5px}
.email{position:absolute;left:693px;top:7px;font-size:10.5px;color:var(--purple);display:flex;align-items:center;gap:5px}
.social{position:absolute;left:928px;top:7px;font-size:10.5px;font-weight:600;color:var(--purple);display:flex;gap:9px}
.brand{position:absolute;left:84px;top:40px;display:flex;align-items:center;gap:8px;font-family:"Titillium Web",sans-serif;font-weight:700;font-size:12px;color:var(--purple-deep)}
.brand-mark{width:44px;height:44px;border-radius:50%;border:5px solid var(--green)}
.phone-btn{position:absolute;left:623px;top:46px;width:157px;height:32px;border:1px solid var(--green);border-radius:16px;background:var(--white);display:flex;align-items:center;justify-content:center;gap:10px;font-family:"Titillium Web",sans-serif;font-weight:700;font-size:14px;letter-spacing:.5px;color:#333}
.cta-btn{position:absolute;left:793px;top:46px;width:202px;height:32px;border-radius:16px;background:var(--green);color:var(--white);display:flex;align-items:center;justify-content:center;gap:8px;font-family:"Titillium Web",sans-serif;font-weight:700;font-size:13px}
.nav{position:absolute;left:0;top:102px;width:1079px;height:42px;background:var(--white);display:flex;padding-left:84px}
.nav a{display:block;padding:0 16px;line-height:42px;font-size:12px;color:var(--nav);text-decoration:none;font-family:"Open Sans",sans-serif}
.nav a.active{border-bottom:2px solid var(--purple)}
.hero{position:absolute;left:0;top:144px;width:1079px;height:360px;background:linear-gradient(100deg,#eeeeec 0%,#e7e3df 35%,#d9c1ab 55%,#ecd9c6 75%,#f1ebe4 100%)}
.hero-copy{position:absolute;left:62px;top:102px}
.hero h1{font-family:"Titillium Web",sans-serif;font-weight:900;font-size:50px;line-height:48px;color:var(--purple-deep);text-transform:uppercase}
.hero p{margin-top:6px;font-family:"Titillium Web",sans-serif;font-weight:700;font-size:19px;color:var(--green);text-transform:uppercase}
.services{position:absolute;left:0;top:504px;width:1079px;height:230px;display:flex}
.service{flex:1;text-align:center;padding-top:15px}
.service:nth-child(1){background:var(--green-soft)}
.service:nth-child(2){background:var(--green)}
.service:nth-child(3){background:var(--purple)}
.service:nth-child(4){background:var(--purple-soft)}
.service-icon{width:93px;height:93px;border-radius:50%;margin:0 auto;background:#e3f98a}
.service:nth-child(n+3) .service-icon{background:#efe4fb}
.service h3{margin-top:15px;font-family:"Titillium Web",sans-serif;font-weight:700;font-size:15px;color:#3d3d1a;text-transform:uppercase}
.service:nth-child(n+3) h3{color:#2d1640}
.service p{margin:6px auto 0;width:220px;font-size:12.5px;line-height:15.5px;color:var(--white)}
.about{position:absolute;left:84px;top:806px;width:445px}
.about h2{font-family:"Titillium Web",sans-serif;font-weight:600;font-size:29px;color:var(--purple);text-transform:uppercase}
.about h2 strong{font-weight:700}
.about p{margin-top:20px;font-size:11.6px;line-height:22.4px;color:var(--text)}
.about p+p{margin-top:28px}
.about a{color:var(--purple);text-decoration:none}
.team-photo{position:absolute;left:540px;top:768px;width:539px;height:408px;background:linear-gradient(90deg,#ffffff 0%,#eef2f5 30%,#e2d5cc 60%,#f3eee9 100%)}
.footer-band{position:absolute;left:0;top:1176px;width:1079px;height:24px;background:#e9f2cf}
</style>
</head>
<body>
<header class="topbar">
  <div class="hours"><svg width="9" height="9" viewBox="0 0 10 10"><path d="M10 0 0 4l4 2 2 4z" fill="#777"/></svg>Hours: Monday - Friday 7:30am - 8pm, Saturday 10am - 5pm, Sunday 10am - 5pm</div>
  <div class="email"><svg width="10" height="8" viewBox="0 0 10 8"><rect width="10" height="8" rx="1" fill="#9a86b8"/><path d="M0 1l5 3 5-3" stroke="#fff" fill="none"/></svg>appointments@thornleighvitality.example</div>
  <div class="social"><span>Linkora</span><span>Zintrel</span><span>Chirpa</span></div>
  <div class="brand"><span class="brand-mark"></span>Thornleigh Vitality Centre</div>
  <div class="phone-btn"><svg width="13" height="13" viewBox="0 0 24 24"><path d="M6.6 10.8a15 15 0 0 0 6.6 6.6l2.2-2.2a1 1 0 0 1 1-.25 11.4 11.4 0 0 0 3.6.6 1 1 0 0 1 1 1V20a1 1 0 0 1-1 1A17 17 0 0 1 3 4a1 1 0 0 1 1-1h3.5a1 1 0 0 1 1 1c0 1.25.2 2.45.6 3.6a1 1 0 0 1-.25 1z" fill="#acd036"/></svg>416-555-0188</div>
  <div class="cta-btn"><span>+</span>MAKE AN APPOINTMENT</div>
</header>
<nav class="nav">
  <a class="active">HOME</a><a>FEES &amp; SERVICES</a><a>OUR STAFF</a><a>NEWS &amp; UPDATES</a><a>CORPORATE WELLNESS</a><a>FORMS</a><a>CONTACT US</a>
</nav>
<section class="hero" role="img" aria-label="Smiling practitioner with a happy young patient in a bright clinic">
  <div class="hero-copy">
    <h1>Bright Path<br>Vitality &amp;<br>Rehab Centre</h1>
    <p>Chiropractic + Physiotherapy + Massage</p>
  </div>
</section>
<section class="services">
  <div class="service"><div class="service-icon" role="img" aria-label="Chiropractic icon"></div><h3>Chiropractic</h3><p>Chiropractic care can help you with neck, back and other joint-related injuries.</p></div>
  <div class="service"><div class="service-icon" role="img" aria-label="Physiotherapy icon"></div><h3>Physiotherapy</h3><p>Physiotherapy can help you recover from a car accident or sports-related injury.</p></div>
  <div class="service"><div class="service-icon" role="img" aria-label="Massage therapy icon"></div><h3>Massage Therapy</h3><p>Massage therapy is one of the oldest forms of natural therapy.</p></div>
  <div class="service"><div class="service-icon" role="img" aria-label="Nutrition icon"></div><h3>Nutritionist</h3><p>Mainstream medicine does not emphasize poor nutrition.</p></div>
</section>
<section class="about">
  <h2><strong>About</strong> Thornleigh Vitality</h2>
  <p>Established in 1989 the Thornleigh Vitality Centre has become one of Canada's leaders in providing quality care and innovative wellness programs for the community. The founder and director Dr. Elias Marrow's vision has come to life with over 30 practitioners providing a multitude of different services under one roof. Some of the services include Chiropractic, Physiotherapy, Athletic Therapy, Naturopathy, Massage Therapy, Acupuncture and Personal Training. The Thornleigh Vitality Centre has a complete Pilates studio on its premises. We also offer many wellness seminars free of cost to the public.</p>
  <p>Our Centre is committed to helping improve and extend the lives of as many people as possible in our community. Come and join our Family and start changing your life today. <a>Read more &gt;</a></p>
</section>
<div class="team-photo" role="img" aria-label="Team of smiling practitioners in white coats"></div>
<div class="footer-band"></div>
</body>
</html>
```